Website design for legal tech start up in Switzerland (B2B)

We are for a legal tech start up in Switzerland called QUORVEL. We have been running since August 2016. This will be our first live website.

We need a website designed and business card design for our start-up in Switzerland. We also need the Web design to be converted into HTML and CSS files.

Function of website:
• To inform potential customers of our services
• Form a key part of our digital marketing and sales footprint.
• Branding

Please find attached logo.

Reason: Looking for more idea's not necessarily set on blue and grey colours only.

Target Market(s)

B2B tech powered legal services.

Industry/Entity Type

Legal

Contact Information for Business Card

Lean and slick design.

Coding

Coded - Design and coding required

Number of Pages Required

5+ page

Requirements
Must have
• VERY LEAN AND CLEAN DESIGN!
• We have received many great standard designs, but we are looking for something more out-of-the box: You can get inspiration from these designs: http://www.plimbergallery.net/websites/clean/
• Thanks!!
• Easy content management system
• Well structured coding for additional development
• Responsive webpage for all types of devices
• SEO optimized
• Tabs (Home, services, team, careers, blog, contact us)
• Colour scheme complementary to logo
Nice to have
• Look and Design - Approachable, High-tech, Modern
• Easy to add chat bot capability in future
Should not have
• Too busy/ too much clutter
• Not take to long to load

```html
<!DOCTYPE html>
<html lang="en">
<head>
<meta charset="utf-8">
<title>QUORVEL – Legal Tech</title>
<link href="https://fonts.googleapis.com/css2?family=Josefin+Sans:wght@600;700&family=Lato:wght@300;400&display=swap" rel="stylesheet">
<style>
  :root {
    --red: #e0312b;
    --white: #ffffff;
    --ink: #3b3b3b;
    --card: #ecece8;
    --dot: #888888;
    --hero-dark: #2b2a2a;
  }
  * { box-sizing: border-box; margin: 0; padding: 0; }
  html, body { width: 1023px; height: 1200px; overflow: hidden; background: var(--white); }
  body { position: relative; font-family: "Lato", sans-serif; color: var(--ink); }

  .hero {
    position: absolute; left: 0; top: 0; width: 1023px; height: 524px;
    background:
      radial-gradient(ellipse at 55% 70%, #8d8a85 0%, #5e5a56 35%, transparent 70%),
      radial-gradient(ellipse at 20% 20%, #5a3a2a 0%, transparent 45%),
      radial-gradient(ellipse at 85% 25%, #7a3a30 0%, transparent 35%),
      linear-gradient(180deg, #3a3938 0%, var(--hero-dark) 100%);
  }
  .brand {
    position: absolute; left: 27px; top: 15px;
    font-family: "Josefin Sans", sans-serif; font-weight: 700;
    font-size: 27px; letter-spacing: 1px; color: var(--white);
  }
  .main-nav { position: absolute; right: 40px; top: 21px; display: flex; gap: 22px; }
  .main-nav a {
    font-family: "Josefin Sans", sans-serif; font-weight: 700; font-size: 12.5px;
    letter-spacing: .6px; color: var(--white); text-decoration: none; text-transform: uppercase;
  }
  .hero-title {
    position: absolute; left: 0; width: 1023px; top: 240px; text-align: center;
    font-family: "Josefin Sans", sans-serif; font-weight: 700; font-size: 24px;
    letter-spacing: 2.6px; color: var(--white); text-transform: uppercase;
  }
  .hero-lead {
    position: absolute; left: 112px; width: 799px; top: 281px; text-align: center;
    font-weight: 300; font-size: 16px; line-height: 19px; letter-spacing: .9px; color: var(--white);
  }
  .btn {
    position: absolute; left: 428px; top: 356px; width: 166px; height: 39px;
    background: var(--red); color: var(--white); border-radius: 2px;
    font-family: "Josefin Sans", sans-serif; font-weight: 700; font-size: 11.5px;
    letter-spacing: 1.2px; text-transform: uppercase; text-decoration: none;
    display: flex; align-items: center; justify-content: center;
  }

  .about-title {
    position: absolute; left: 0; width: 1023px; top: 585px; text-align: center;
    font-family: "Josefin Sans", sans-serif; font-weight: 700; font-size: 15.5px;
    letter-spacing: 2px; color: var(--red); text-transform: uppercase;
  }
  .about-text {
    position: absolute; left: 20px; width: 983px; top: 620px; text-align: center;
    font-size: 13.4px; line-height: 21px; letter-spacing: .6px; color: var(--ink);
  }

  .team { position: absolute; left: 39px; top: 778px; display: flex; gap: 10px; }
  .member { width: 228px; }
  .member-photo { height: 232px; }
  .member:nth-child(1) .member-photo { background: linear-gradient(180deg, #ffffff 0%, #d9cfc8 45%, #3a2a24 100%); }
  .member:nth-child(2) .member-photo { background: linear-gradient(180deg, #ffffff 0%, #c9aa90 45%, #252428 100%); }
  .member:nth-child(3) .member-photo { background: linear-gradient(180deg, #ffffff 0%, #e4d4bc 45%, #22222a 100%); }
  .member:nth-child(4) .member-photo { background: linear-gradient(180deg, #ffffff 0%, #d8c2b2 45%, #2c2c2c 100%); }
  .member-info { height: 132px; background: var(--card); text-align: center; padding-top: 36px; }
  .member-name {
    font-family: "Josefin Sans", sans-serif; font-weight: 700; font-size: 15px;
    letter-spacing: 1.3px; color: var(--red); text-transform: uppercase;
  }
  .member-role { margin-top: 9px; font-size: 12px; line-height: 15px; color: #222; }

  .pager { position: absolute; left: 506px; top: 1191px; display: flex; gap: 5px; }
  .pager span { width: 8px; height: 8px; border-radius: 50%; border: 1.3px solid var(--dot); }
  .pager span.is-active { background: var(--dot); }
</style>
</head>
<body>
  <header class="hero" role="img" aria-label="Desk scene with leather bag, glasses, phone, laptop, red coffee cup and an open notebook with pen">
    <div class="brand">QUORVEL</div>
    <nav class="main-nav">
      <a href="#">Home</a><a href="#">About</a><a href="#">Services</a><a href="#">Careers</a><a href="#">Blog</a><a href="#">Contact</a>
    </nav>
    <h1 class="hero-title">Main branding text in large fonts goes</h1>
    <p class="hero-lead">Since 2009 we have been developing software for our clients and ourselves with the philosophy<br>that we should act like we are part of your business.</p>
    <a class="btn" href="#">Learn more</a>
  </header>

  <h2 class="about-title">About us</h2>
  <p class="about-text">We`ve spent the last decade working with start-ups and companies just like yours, and we've developed<br>an approach that blends the fast and responsive software development life cycle with proven and robust methodologies (and code) to give you<br>the edge you're looking for all the while building software (and your business) that you can grow with and count on.</p>

  <section class="team">
    <article class="member">
      <div class="member-photo" role="img" aria-label="Portrait of team member"></div>
      <div class="member-info"><h3 class="member-name">Elena Varga</h3><p class="member-role">Litigation, Real Estate,<br>Injuries &amp; Tax Disputes</p></div>
    </article>
    <article class="member">
      <div class="member-photo" role="img" aria-label="Portrait of team member"></div>
      <div class="member-info"><h3 class="member-name">Elena Varga</h3><p class="member-role">Litigation, Real Estate,<br>Injuries &amp; Tax Disputes</p></div>
    </article>
    <article class="member">
      <div class="member-photo" role="img" aria-label="Portrait of team member"></div>
      <div class="member-info"><h3 class="member-name">Elena Varga</h3><p class="member-role">Litigation, Real Estate,<br>Injuries &amp; Tax Disputes</p></div>
    </article>
    <article class="member">
      <div class="member-photo" role="img" aria-label="Portrait of team member"></div>
      <div class="member-info"><h3 class="member-name">Elena Varga</h3><p class="member-role">Litigation, Real Estate,<br>Injuries &amp; Tax Disputes</p></div>
    </article>
  </section>

  <div class="pager"><span class="is-active"></span><span></span><span></span></div>
</body>
</html>
```